SUMMIT GATHERING 2021. August 20th -22nd.

The Hosts of the conference: Grace Tabernacle-Pastors Ron n Della ( Picture with two persons)

Guest Minister: Bishop Lucinda Okotieno. (Cedar Ridge Awakening)

Venue:
Sealand Gateway Lodgeview. 4817 North 239th Avenue Seattle, WA 98174.

Conference times.
Friday August 20th 6pm-8:30pm
Saturday August 21st. 6pm-8:30pm

Sunday August 22nd 10am-1pm
“ CHURCH RENEWAL GATHERING”

5pm-7:30pm
TWOFOLD SURGE GATHERING.

Target Market(s)

18-55

Industry/Entity Type

Religious/ Entertainment.

Requirements
Must have
• A highlight of the Relaunch service on Sunday August 22nd 5pm-7:30pm.
Nice to have
• Excellent ideas….

```html
<!DOCTYPE html>
<html lang="en">
<head>
<meta charset="utf-8">
<title>Summit Gathering 2021 – Church Renewal Gathering</title>
<link rel="stylesheet" href="https://fonts.googleapis.com/css2?family=Montserrat:wght@900&family=Open+Sans:wght@400;700;800&family=Pinyon+Script&display=swap">
<style>
  :root {
    --ink-white: #ffffff;
    --tan: #c39c72;
    --umber: #5a381c;
    --outline: #6b4426;
    --bg-glow: #b07a4a;
    --bg-mid: #5a3220;
    --bg-deep: #1f0f0d;
    --bg-base: #170b0a;
    --rule: #ffffff;
  }
  * { margin: 0; padding: 0; box-sizing: border-box; }
  html, body { width: 849px; height: 1200px; overflow: hidden; background: var(--bg-base); }
  .poster {
    position: relative;
    width: 849px;
    height: 1200px;
    overflow: hidden;
    font-family: "Open Sans", Arial, sans-serif;
    color: var(--ink-white);
  }
  .backdrop {
    position: absolute; inset: 0;
    background:
      radial-gradient(ellipse 260px 380px at 500px 200px, rgba(255,220,170,.55), rgba(255,220,170,0) 70%),
      radial-gradient(ellipse 700px 560px at 430px 230px, var(--bg-glow), var(--bg-mid) 45%, var(--bg-deep) 80%),
      var(--bg-base);
  }
  .backdrop::after {
    content: ""; position: absolute; left: 0; right: 0; top: 560px; bottom: 0;
    background: linear-gradient(180deg, rgba(23,11,10,0) 0%, rgba(40,20,16,.5) 50%, rgba(23,11,10,.85) 100%);
  }
  .abs { position: absolute; line-height: 1; white-space: nowrap; }
  .event-name { left: 0; right: 0; top: 36px; text-align: center; font-weight: 700; font-size: 42px; letter-spacing: .5px; }
  .event-year { left: 0; right: 0; top: 90px; text-align: center; font-weight: 800; font-size: 70px; }
  .event-dates { left: 0; right: 0; top: 204px; text-align: center; font-weight: 800; font-size: 32px; color: var(--umber); }
  .event-dates sup { font-size: 17px; vertical-align: 13px; }
  .headline-main {
    left: 0; right: 0; top: 268px; text-align: center;
    font-family: "Montserrat", Arial, sans-serif; font-weight: 900; font-size: 137px; letter-spacing: -2px;
    color: var(--ink-white);
    -webkit-text-stroke: 2px var(--outline);
    paint-order: stroke fill;
    text-shadow: 0 0 3px var(--outline), 0 0 3px var(--outline);
  }
  .headline-sub { left: 0; right: 0; top: 401px; text-align: center; font-weight: 700; font-size: 88px; color: var(--tan); letter-spacing: -1px; }
  .headline-script { left: 360px; top: 452px; font-family: "Pinyon Script", cursive; font-size: 92px; color: var(--ink-white); }

  .column-rule { position: absolute; left: 424px; top: 625px; width: 1.5px; height: 228px; background: var(--rule); }
  .schedule { position: absolute; right: 448px; top: 626px; text-align: right; }
  .details { position: absolute; left: 446px; top: 626px; text-align: left; }
  .label { font-weight: 800; font-size: 25px; color: var(--tan); line-height: 1.05; letter-spacing: -.3px; }
  .line { font-size: 19px; line-height: 26px; }
  .schedule .slot { margin-top: 17px; }
  .schedule .slot:first-of-type { margin-top: 4px; }
  .details .address { margin-top: 4px; }
  .details .label-block { margin-top: 15px; }

  .portrait {
    position: absolute; width: 186px; height: 186px; border-radius: 50%;
    border: 1.5px solid var(--ink-white);
  }
  .portrait.hosts { left: 86px; top: 906px; background: radial-gradient(circle at 40% 45%, #6b4a3c, #3a2530 60%, #a0467f 100%); }
  .portrait.guest { left: 584px; top: 906px; background: radial-gradient(circle at 50% 40%, #5a3a2a, #b8b4b0 60%, #e8e8e6 100%); }

  .ministry-mark { position: absolute; left: 350px; top: 985px; width: 149px; text-align: center; }
  .ministry-mark .dot { display: inline-block; width: 12px; height: 12px; background: var(--tan); vertical-align: middle; margin-right: 6px; }
  .ministry-mark .name { font-weight: 700; font-size: 14px; color: var(--tan); vertical-align: middle; }

  .caption { position: absolute; text-align: center; font-weight: 700; }
  .caption.hosts { left: 0; width: 358px; top: 1112px; }
  .caption.guest { left: 500px; width: 354px; top: 1107px; }
  .caption .small { font-size: 15px; line-height: 21px; }
  .caption .big { font-size: 19px; line-height: 26px; }
</style>
</head>
<body>
<main class="poster">
  <div class="backdrop" role="img" aria-label="Warm church interior with sunlight streaming through arched windows"></div>

  <h1 class="abs event-name">SUMMIT GATHERING</h1>
  <div class="abs event-year">2021</div>
  <div class="abs event-dates">AUGUST 20<sup>TH</sup> -22<sup>ND</sup></div>

  <div class="abs headline-main">CHURCH</div>
  <div class="abs headline-sub">RENEWAL</div>
  <div class="abs headline-script">Gathering</div>

  <section class="schedule">
    <div class="label">CONFERENCE TIMES</div>
    <div class="slot"><div class="line">Friday August 20th</div><div class="line">6pm-8:30pm</div></div>
    <div class="slot"><div class="line">Saturday August 21st</div><div class="line">6pm-8:30pm</div></div>
    <div class="slot"><div class="line">Sunday August 22nd</div><div class="line">10am-1pm</div></div>
  </section>

  <div class="column-rule"></div>

  <section class="details">
    <div class="label">VENUE</div>
    <div class="address">
      <div class="line">Sealand Gateway Lodgeview. 4817</div>
      <div class="line">North 239th Avenue Seattle,</div>
      <div class="line">WA 98174.</div>
    </div>
    <div class="label-block">
      <div class="label">TWOFOLD<br>SURGE GATHERING.</div>
      <div class="line">Sunday August 22nd</div>
      <div class="line">5pm-7:30pm</div>
    </div>
  </section>

  <div class="portrait hosts" role="img" aria-label="Portrait photo of the hosting pastors"></div>
  <div class="ministry-mark"><span class="dot"></span><span class="name">Grace Tabernacle</span></div>
  <div class="portrait guest" role="img" aria-label="Portrait photo of the guest minister"></div>

  <div class="caption hosts">
    <div class="small">The Hosts</div>
    <div class="small">of the conference:</div>
    <div class="big">Grace Tabernacle-Pastors Ron n Della</div>
  </div>
  <div class="caption guest">
    <div class="small">Guest Minister</div>
    <div class="big">Bishop Lucinda Okotieno</div>
    <div class="big">(Cedar Ridge Awakening)</div>
  </div>
</main>
</body>
</html>
```